Brightstone Roofing Business Card

This is my current business card. But I’d like to make some changes. Somewhere on the card I’d like to list some of the services we offer. Maybe on the back? But I’d still like to keep the red. White and black modern look.

-residential & commercial roofing
-Roof Repairs & Maintenance
-Storm Damage & Insurance Claims specialist
-Christmas Lights and permanent Christmas lights
Fencing. Windows. Gutters. Siding. Sheetrock, painting.

```html
<!DOCTYPE html>
<html lang="en">
<head>
<meta charset="UTF-8">
<title>Brightstone Roofing Business Card</title>
<link rel="stylesheet" href="https://fonts.googleapis.com/css2?family=Poppins:wght@400;500;600;700&family=Russo+One&display=swap">
<style>
  :root {
    --backdrop: #2b2b2d;
    --red-light: #d21b24;
    --red-mid: #a50d14;
    --red-deep: #5e0004;
    --ink: #0b0b0b;
    --ink-soft: #1d1d1f;
    --white: #ffffff;
    --grey-text: #d8d8d8;
    --card-w: 700px;
    --card-h: 400px;
  }
  * { box-sizing: border-box; margin: 0; padding: 0; }
  html, body {
    width: 1200px; height: 900px; overflow: hidden;
    background: var(--backdrop);
    font-family: "Poppins", sans-serif;
  }
  .canvas {
    position: relative; width: 1200px; height: 900px;
  }
  .card {
    position: absolute; left: 250px;
    width: var(--card-w); height: var(--card-h);
    overflow: hidden;
    box-shadow: 0 18px 40px rgba(0,0,0,0.45);
  }

  /* Front side */
  .card-front {
    top: 40px;
    border-radius: 48px 0 48px 0;
    background: linear-gradient(125deg, var(--red-light) 0%, var(--red-mid) 45%, var(--red-deep) 100%);
  }
  .front-brand {
    position: absolute; right: 56px; top: 132px; width: 330px;
    text-align: left;
  }
  .front-brand .wordmark {
    font-family: "Poppins", sans-serif; font-weight: 700;
    color: var(--ink); line-height: 1.05;
    font-size: 40px; letter-spacing: 1px; text-transform: uppercase;
  }
  .front-brand .wordmark span { display: block; font-size: 29px; letter-spacing: 4px; }
  .front-brand .rule {
    margin: 22px 0 16px; height: 1px;
    background: rgba(255,255,255,0.25);
  }
  .front-brand .web {
    font-weight: 600; font-size: 15px; letter-spacing: 4.2px;
    color: var(--ink);
  }

  /* Back side */
  .card-back {
    top: 460px;
    border-radius: 0 48px 0 48px;
    background: linear-gradient(120deg, var(--ink) 0%, var(--ink-soft) 100%);
    color: var(--white);
  }
  .holder { position: absolute; left: 44px; top: 40px; }
  .holder-name {
    font-family: "Russo One", sans-serif; font-size: 30px;
    letter-spacing: 1px; line-height: 1;
  }
  .holder-name .first { color: var(--red-light); }
  .holder-role { font-size: 13px; letter-spacing: 1px; color: var(--grey-text); margin-top: 4px; }

  .contact-list { list-style: none; margin-top: 20px; }
  .contact-list li {
    display: flex; align-items: center; gap: 10px;
    font-size: 14px; line-height: 1.65; color: var(--white);
  }
  .contact-list svg { width: 14px; height: 14px; flex: none; }

  .services { margin-top: 20px; }
  .services-title {
    font-family: "Russo One", sans-serif; font-size: 17px;
    color: var(--red-light); letter-spacing: 1px; margin-bottom: 4px;
  }
  .services-list { list-style: none; }
  .services-list li {
    display: flex; align-items: center; gap: 9px;
    font-size: 12.5px; line-height: 1.6; color: var(--white);
  }
  .hatch {
    width: 12px; height: 9px; flex: none;
    background: repeating-linear-gradient(120deg, var(--red-light) 0 2px, transparent 2px 4px);
  }

  .back-brand {
    position: absolute; right: 52px; top: 110px;
    display: flex; flex-direction: column; align-items: center; gap: 18px;
  }
  .brand-dot {
    width: 110px; height: 110px; border-radius: 50%;
    background: var(--red-light);
  }
  .back-brand .wordmark {
    font-family: "Poppins", sans-serif; font-weight: 700;
    color: var(--white); text-align: center; text-transform: uppercase;
    font-size: 30px; line-height: 1.05; letter-spacing: 1px;
  }
  .back-brand .wordmark span { display: block; font-size: 22px; letter-spacing: 3px; }
</style>
</head>
<body>
<main class="canvas">

  <section class="card card-front" aria-label="Card front">
    <div class="front-brand">
      <p class="wordmark">Brightstone <span>Roofing Co.</span></p>
      <div class="rule"></div>
      <p class="web">www.brightstoneroofing.co</p>
    </div>
  </section>

  <section class="card card-back" aria-label="Card back">
    <div class="holder">
      <h1 class="holder-name"><span class="first">DALE</span> MERCER</h1>
      <p class="holder-role">OWNER</p>

      <ul class="contact-list">
        <li>
          <svg viewBox="0 0 24 24" aria-hidden="true"><path fill="#d21b24" d="M6.6 10.8a15.1 15.1 0 0 0 6.6 6.6l2.2-2.2a1 1 0 0 1 1-.25 11.4 11.4 0 0 0 3.6.57 1 1 0 0 1 1 1V20a1 1 0 0 1-1 1A17 17 0 0 1 3 4a1 1 0 0 1 1-1h3.5a1 1 0 0 1 1 1c0 1.25.2 2.45.57 3.57a1 1 0 0 1-.25 1z"/></svg>
          555-014-2290
        </li>
        <li>
          <svg viewBox="0 0 24 24" aria-hidden="true"><rect x="2" y="5" width="20" height="14" rx="2" fill="#d21b24"/><path d="M3 6l9 7 9-7" fill="none" stroke="#0b0b0b" stroke-width="2"/></svg>
          dale@brightstoneroofing.co
        </li>
        <li>
          <svg viewBox="0 0 24 24" aria-hidden="true"><g fill="none" stroke="#d21b24" stroke-width="2"><circle cx="12" cy="12" r="9"/><path d="M3 12h18M12 3c3 3.5 3 14.5 0 18M12 3c-3 3.5-3 14.5 0 18"/></g></svg>
          www.brightstoneroofing.co
        </li>
      </ul>

      <div class="services">
        <h2 class="services-title">SERVICES</h2>
        <ul class="services-list">
          <li><span class="hatch"></span>Residential &amp; Commercial Roofing</li>
          <li><span class="hatch"></span>Roof Repairs &amp; Maintenance</li>
          <li><span class="hatch"></span>Storm Damage &amp; Insurance Claims Specialist</li>
          <li><span class="hatch"></span>Christmas Lights And Permanent Christmas Lights</li>
          <li><span class="hatch"></span>Fencing. Windows. Gutters</li>
          <li><span class="hatch"></span>Siding. Sheetrock, painting</li>
        </ul>
      </div>
    </div>

    <div class="back-brand">
      <div class="brand-dot"></div>
      <p class="wordmark">Brightstone <span>Roofing Co.</span></p>
    </div>
  </section>

</main>
</body>
</html>
```